Business card for apparel company. Specializing in fishing and boating performance wear. Main company name is Marlow Pelican Company, LLC brand name for apparel is TIDEWAKE. See website www.TidewakeBayline.com I will attach some logos to consider.

```html
<!DOCTYPE html>
<html lang="en">
<head>
<meta charset="utf-8">
<title>Tidewake Business Card</title>
<link href="https://fonts.googleapis.com/css2?family=Poppins:wght@400;500;700;800&display=swap" rel="stylesheet">
<style>
  :root {
    --page-bg: #ececec;
    --blue-light: #05a8e8;
    --blue-mid: #0a8fe0;
    --blue-deep: #0566d6;
    --ink: #1b1b1b;
    --white: #ffffff;
  }
  * { margin: 0; padding: 0; box-sizing: border-box; }
  html, body {
    width: 1200px; height: 900px; overflow: hidden;
    background: var(--page-bg);
    font-family: "Poppins", sans-serif;
  }
  .sheet {
    width: 1200px; height: 900px;
    display: flex; flex-direction: column;
    align-items: center; justify-content: center; gap: 34px;
  }
  .card {
    position: relative;
    width: 700px; height: 400px;
    overflow: hidden;
    box-shadow: 0 8px 24px rgba(0,0,0,0.18);
  }
  /* Front */
  .card-front {
    background: linear-gradient(180deg, var(--blue-light) 0%, var(--blue-deep) 100%);
    display: flex; align-items: center; justify-content: center;
  }
  .front-wordmark {
    color: var(--white);
    font-weight: 800;
    font-size: 74px;
    letter-spacing: 4px;
  }
  /* Back */
  .card-back { background: var(--white); }
  .wave { position: absolute; left: 0; top: 0; width: 700px; height: 400px; }
  .back-wordmark {
    position: absolute; right: 44px; top: 96px;
    color: var(--blue-mid);
    font-weight: 800; font-size: 50px; letter-spacing: 2px;
  }
  .holder { position: absolute; left: 56px; top: 66px; }
  .holder-name {
    color: var(--blue-mid);
    font-weight: 700; font-size: 25px; letter-spacing: 0.5px; line-height: 1.1;
  }
  .holder-title { color: var(--ink); font-size: 16px; font-weight: 400; }
  .contacts { position: absolute; left: 56px; top: 168px; list-style: none; }
  .contacts li {
    display: flex; align-items: center; gap: 10px;
    color: var(--ink); font-size: 17px; line-height: 1.5;
  }
  .contacts svg { width: 20px; height: 20px; flex: none; }
  .address {
    position: absolute; left: 86px; top: 240px;
    color: var(--ink); font-size: 17px; line-height: 1.35;
  }
  .website {
    position: absolute; right: 38px; bottom: 46px;
    color: var(--white); font-size: 15px; font-weight: 500;
  }
</style>
</head>
<body>
<main class="sheet">
  <section class="card card-front">
    <div class="front-wordmark">TIDEWAKE</div>
  </section>

  <section class="card card-back">
    <svg class="wave" viewBox="0 0 700 400" aria-hidden="true">
      <defs>
        <linearGradient id="waveFill" x1="0" y1="0" x2="0" y2="1">
          <stop offset="0" stop-color="#06a9e9"/>
          <stop offset="1" stop-color="#0a74dc"/>
        </linearGradient>
      </defs>
      <path d="M0,312 C230,312 400,275 490,225 C400,290 230,338 0,340 Z" fill="#0566d6"/>
      <path d="M0,352 C250,350 420,300 520,225 C590,175 640,150 700,140 L700,400 L0,400 Z" fill="url(#waveFill)"/>
    </svg>

    <div class="back-wordmark">TIDEWAKE</div>

    <div class="holder">
      <p class="holder-name">ELIAS MARREN</p>
      <p class="holder-title">Managing Director</p>
    </div>

    <ul class="contacts">
      <li>
        <svg viewBox="0 0 24 24"><path fill="#0a8fe0" d="M6.6 10.8a15.1 15.1 0 0 0 6.6 6.6l2.2-2.2c.3-.3.7-.4 1-.2 1.1.4 2.3.6 3.6.6.6 0 1 .4 1 1V20c0 .6-.4 1-1 1A17 17 0 0 1 3 4c0-.6.4-1 1-1h3.5c.6 0 1 .4 1 1 0 1.3.2 2.5.6 3.6.1.3 0 .7-.2 1z"/></svg>
        044-555 010 274
      </li>
      <li>
        <svg viewBox="0 0 24 24"><rect x="2" y="5" width="20" height="14" fill="#0a8fe0"/><path d="M2 5l10 8 10-8" fill="none" stroke="#fff" stroke-width="1.6"/></svg>
        info@tidewakebayline.com
      </li>
    </ul>

    <p class="address">88 Harbor Row<br>Gulf Shores, 36542</p>

    <p class="website">www.TidewakeBayline.com</p>
  </section>
</main>
</body>
</html>
```